Powerpoint Slide Deck

I had my logo designed using artfolda and would like to have a professional looking powerpoint deck created with my logo etc. my website is brovana.info

```html
<!DOCTYPE html>
<html lang="en">
<head>
<meta charset="utf-8">
<title>Brovana – Slide Deck</title>
<link href="https://fonts.googleapis.com/css2?family=Ubuntu:wght@400;500;700&family=Open+Sans:wght@400;600;700&display=swap" rel="stylesheet">
<style>
:root{
  --page:#e4e4e4;
  --slide:#ffffff;
  --ink:#111418;
  --body:#2b2f36;
  --blue:#1b6fc4;
  --blue-dark:#0f4f96;
  --green:#6cb33f;
  --purple:#5a2d8c;
  --orange:#f29a1f;
  --muted:#6b7280;
}
*{box-sizing:border-box;margin:0;padding:0}
html,body{width:1200px;height:4076px;overflow:hidden}
body{background:var(--page);position:relative;font-family:"Open Sans",Arial,sans-serif;color:var(--body)}
.slide{position:absolute;left:30px;width:1140px;height:648px;background:var(--slide);overflow:hidden;box-shadow:0 2px 6px rgba(0,0,0,.12)}
.slide-rule{position:absolute;left:0;right:0;bottom:26px;height:3px;background:var(--blue)}
.brand{position:absolute;z-index:2;display:flex;align-items:center;gap:6px;font-family:"Ubuntu",sans-serif;font-weight:700;font-size:20px;color:var(--blue-dark)}
.brand-dot{width:12px;height:12px;border-radius:50%;background:var(--green)}
.heading{font-family:"Ubuntu",sans-serif;font-weight:700;color:var(--ink);position:absolute;z-index:2;white-space:nowrap}

/* welcome */
.s-welcome{top:16px}
.s-welcome .brand{left:40px;top:34px}
.welcome-kicker{left:40px;top:100px;font-size:74px}
.welcome-name{left:36px;top:180px;font-size:124px;letter-spacing:-1px}
.welcome-copy{position:absolute;left:42px;top:352px;width:560px;font-size:13px;line-height:1.45}
.welcome-copy p+p{margin-top:12px}
.welcome-photo{position:absolute;right:0;top:0;width:470px;height:648px;background:linear-gradient(135deg,#c9dde8 0%,#7fa3b8 45%,#3d5a6e 100%)}

/* why */
.s-why{top:688px}
.s-why .brand{right:34px;top:30px}
.why-illustration{position:absolute;left:40px;top:130px;width:390px;height:330px;border-radius:8px;background:linear-gradient(160deg,#f6e4d4 0%,#e9b889 50%,#c1553b 100%)}
.why-title{left:470px;top:120px;font-size:56px}
.why-copy{position:absolute;left:470px;top:205px;width:620px;font-size:19px;line-height:1.4;color:var(--body)}

/* solutions */
.s-solutions{top:1360px}
.s-solutions .brand{right:34px;top:36px}
.solutions-title{left:40px;top:26px;font-size:58px}
.solutions-laptop{position:absolute;left:70px;top:190px;width:400px;height:250px;border-radius:6px;background:linear-gradient(180deg,#3a4a5c 0%,#5f8f6a 55%,#1e2833 100%)}
.solutions-links{position:absolute;left:0;top:0;z-index:1}
.solution{position:absolute;left:660px;width:420px;z-index:2}
.solution h3{font-family:"Ubuntu",sans-serif;font-weight:700;font-size:27px;color:var(--blue)}
.solution p{font-size:17px;line-height:1.35;margin-top:4px}

/* partners */
.s-partners{top:2032px}
.s-partners .brand{right:34px;top:34px}
.partners-title{left:40px;top:22px;font-size:58px}
.partners-rings{position:absolute;left:0;top:0;z-index:1}
.partner-name{position:absolute;z-index:2;top:316px;width:190px;text-align:center;font-family:"Ubuntu",sans-serif;font-weight:700;font-size:22px;color:var(--ink)}

/* testimonials */
.s-testimonials{top:2704px}
.s-testimonials .brand{right:34px;top:36px}
.testimonials-title{left:40px;top:22px;font-size:58px}
.testimonials-sub{position:absolute;left:0;right:0;top:120px;text-align:center;font-family:"Ubuntu",sans-serif;font-weight:700;font-size:38px;color:var(--ink)}
.quote-card{position:absolute;top:210px;width:300px;padding:22px 22px;background:#fff}
.quote-card.is-featured{border:1px solid #d5d8dd;box-shadow:0 4px 14px rgba(0,0,0,.12);top:200px;padding-top:32px;padding-bottom:32px}
.quote-name{font-family:"Ubuntu",sans-serif;font-weight:700;font-size:19px;color:var(--ink);text-transform:uppercase}
.quote-text{margin-top:14px;font-size:17px;line-height:1.4}

/* thanks */
.s-thanks{top:3376px}
.thanks-photo{position:absolute;left:0;top:0;width:560px;height:648px;background:linear-gradient(150deg,#5d6f75 0%,#2c3a40 55%,#11181c 100%)}
.thanks-panel{position:absolute;left:560px;top:0;right:0;height:648px;background:linear-gradient(135deg,#1a6fb8 0%,#1e8f9a 30%,#3aa54c 65%,#58b848 100%)}
.thanks-title{position:absolute;left:58px;top:124px;font-family:"Ubuntu",sans-serif;font-weight:700;font-size:76px;color:#fff;letter-spacing:1px;white-space:nowrap}
.contact{position:absolute;left:60px;display:flex;align-items:center;gap:24px;color:#fff;font-size:17px;line-height:1.4;width:460px}
.contact-icon{flex:none;width:44px;height:44px;border-radius:50%;background:var(--orange);display:flex;align-items:center;justify-content:center}
</style>
</head>
<body>

<section class="slide s-welcome">
  <div class="brand"><span class="brand-dot"></span>Brovana</div>
  <h1 class="heading welcome-kicker">Welcome to</h1>
  <div class="heading welcome-name">Brovana</div>
  <div class="welcome-copy">
    <p>In a complex world of IT, Brovana will assist you in optimizing IT spend. Our 20 years in the IT industry brings best of breed personnel from Data Center, Managed Services, and Disaster Recovery, to help you get the best solutions for the best price.</p>
    <p>In a complex world of IT, let us help simplify.</p>
  </div>
  <div class="welcome-photo" role="img" aria-label="Photo of a smiling consultant holding a laptop in a bright server room"></div>
  <div class="slide-rule"></div>
</section>

<section class="slide s-why">
  <div class="brand"><span class="brand-dot"></span>Brovana</div>
  <div class="why-illustration" role="img" aria-label="Illustration of a person working at a desk with large code screens"></div>
  <h2 class="heading why-title">Why Brovana</h2>
  <p class="why-copy">It's Simple. Our resources have years of experience understanding IT environments. All of our staff have been top of their class in each of their specialties and can help you optimize your spend with best of breed solutioning. Our staff have unmatched knowledge in Networking, Security, Data Center, Disaster Recovery, Kestrel Solutions, Hyperscaler Solutions, Managed Services, and more. The people we put in front of you are the best of the best in IT. Let our team help you optimize your environment.</p>
  <div class="slide-rule"></div>
</section>

<section class="slide s-solutions">
  <h2 class="heading solutions-title">Our Solutions</h2>
  <div class="brand"><span class="brand-dot"></span>Brovana</div>
  <div class="solutions-laptop" role="img" aria-label="Photo of an open laptop showing a landscape wallpaper"></div>
  <svg class="solutions-links" width="1140" height="648" aria-hidden="true">
    <path d="M520 150 Q 560 110 610 140 M610 140 Q 560 210 610 290 Q 560 370 610 450" fill="none" stroke="#7a9cc6" stroke-width="2" stroke-dasharray="6 6"/>
    <circle cx="520" cy="150" r="6" fill="#1b6fc4"/>
    <g fill="#1b6fc4">
      <polygon points="610,118 632,131 632,157 610,170 588,157 588,131"/>
      <polygon points="610,264 632,277 632,303 610,316 588,303 588,277"/>
      <polygon points="610,424 632,437 632,463 610,476 588,463 588,437"/>
    </g>
    <g fill="none" stroke="#fff" stroke-width="2">
      <circle cx="610" cy="144" r="8"/>
      <path d="M598 296 h24 a6 6 0 0 0 -6 -10 a8 8 0 0 0 -14 2 a5 5 0 0 0 -4 8z"/>
      <rect x="600" y="440" width="20" height="8"/><rect x="600" y="452" width="20" height="8"/>
    </g>
  </svg>
  <div class="solution" style="top:118px"><h3>Managed Services</h3><p>Should you manage internally or should you hire an expert to manage?</p></div>
  <div class="solution" style="top:264px"><h3>Cloud</h3><p>In todays quickly changing IT environment companies have a lot of choices.</p></div>
  <div class="solution" style="top:424px"><h3>Data Center</h3><p>Should you be in the Data Center business?</p></div>
  <div class="slide-rule"></div>
</section>

<section class="slide s-partners">
  <svg class="partners-rings" width="1140" height="648" aria-hidden="true">
    <g transform="translate(150 328)">
      <circle r="100" fill="#fff" stroke="#e3e6ea" stroke-width="2"/>
      <circle r="118" fill="none" stroke="var(--green)" stroke-width="14" stroke-dasharray="180 562" transform="rotate(-150)"/>
      <circle r="118" fill="none" stroke="var(--blue)" stroke-width="14" stroke-dasharray="120 622" transform="rotate(20)"/>
      <circle r="118" fill="none" stroke="var(--purple)" stroke-width="14" stroke-dasharray="90 652" transform="rotate(100)"/>
    </g>
    <g transform="translate(415 328)">
      <circle r="100" fill="#fff" stroke="#e3e6ea" stroke-width="2"/>
      <circle r="118" fill="none" stroke="var(--green)" stroke-width="14" stroke-dasharray="160 582" transform="rotate(-120)"/>
      <circle r="118" fill="none" stroke="var(--blue)" stroke-width="14" stroke-dasharray="110 632" transform="rotate(30)"/>
      <circle r="118" fill="none" stroke="var(--purple)" stroke-width="14" stroke-dasharray="100 642" transform="rotate(110)"/>
    </g>
    <g transform="translate(690 328)">
      <circle r="100" fill="#fff" stroke="#e3e6ea" stroke-width="2"/>
      <circle r="118" fill="none" stroke="var(--green)" stroke-width="14" stroke-dasharray="170 572" transform="rotate(-140)"/>
      <circle r="118" fill="none" stroke="var(--blue)" stroke-width="14" stroke-dasharray="130 612" transform="rotate(15)"/>
      <circle r="118" fill="none" stroke="var(--purple)" stroke-width="14" stroke-dasharray="90 652" transform="rotate(105)"/>
    </g>
    <g transform="translate(960 328)">
      <circle r="100" fill="#fff" stroke="#e3e6ea" stroke-width="2"/>
      <circle r="118" fill="none" stroke="var(--green)" stroke-width="14" stroke-dasharray="170 572" transform="rotate(-130)"/>
      <circle r="118" fill="none" stroke="var(--blue)" stroke-width="14" stroke-dasharray="120 622" transform="rotate(25)"/>
      <circle r="118" fill="none" stroke="var(--purple)" stroke-width="14" stroke-dasharray="95 647" transform="rotate(108)"/>
    </g>
  </svg>
  <h2 class="heading partners-title">Our Partners</h2>
  <div class="brand"><span class="brand-dot"></span>Brovana</div>
  <div class="partner-name" style="left:55px">Telvora</div>
  <div class="partner-name" style="left:320px">Skyforge Cloud</div>
  <div class="partner-name" style="left:595px">Netrion</div>
  <div class="partner-name" style="left:865px">Quadrasoft</div>
  <div class="slide-rule"></div>
</section>

<section class="slide s-testimonials">
  <h2 class="heading testimonials-title">Testimonials</h2>
  <div class="brand"><span class="brand-dot"></span>Brovana</div>
  <div class="testimonials-sub">What Do Our Partners Have To Say</div>
  <article class="quote-card" style="left:90px">
    <div class="quote-name">Dana Whitlock.</div>
    <p class="quote-text">"Not only did Merriton meet the financial targets for our program; they in fact exceeded them by 25% with respect to net profit. Additionally, I have seen firsthand the improvement in the quality of our offerings in presentation, taste and nutritional content."</p>
  </article>
  <article class="quote-card is-featured" style="left:420px">
    <div class="quote-name">Dana Whitlock.</div>
    <p class="quote-text">"Not only did Merriton meet the financial targets for our program; they in fact exceeded them by 25% with respect to net profit. Additionally, I have seen firsthand the improvement in the quality of our offerings in presentation, taste and nutritional content."</p>
  </article>
  <article class="quote-card" style="left:750px">
    <div class="quote-name">Dana Whitlock.</div>
    <p class="quote-text">"Not only did Merriton meet the financial targets for our program; they in fact exceeded them by 25% with respect to net profit. Additionally, I have seen firsthand the improvement in the quality of our offerings in presentation, taste and nutritional content."</p>
  </article>
  <div class="slide-rule"></div>
</section>

<section class="slide s-thanks">
  <div class="thanks-photo" role="img" aria-label="Photo of hands typing on a laptop with glowing gear graphics"></div>
  <div class="thanks-panel">
    <h2 class="thanks-title">THANK YOU</h2>
    <div class="contact" style="top:280px">
      <span class="contact-icon"><svg width="20" height="20" viewBox="0 0 20 20"><path d="M10 1a6 6 0 0 0-6 6c0 5 6 12 6 12s6-7 6-12a6 6 0 0 0-6-6z" fill="#fff"/><circle cx="10" cy="7" r="2.2" fill="#f29a1f"/></svg></span>
      <span>1417 Lorem ipsum dolor sit amet, consectetur adipiscing elit</span>
    </div>
    <div class="contact" style="top:372px">
      <span class="contact-icon"><svg width="20" height="20" viewBox="0 0 20 20"><path d="M4 2h4l2 5-2.5 1.5a11 11 0 0 0 4 4L13 10l5 2v4a2 2 0 0 1-2 2A15 15 0 0 1 2 4a2 2 0 0 1 2-2z" fill="#fff"/></svg></span>
      <span>+1 888 8888 8888</span>
    </div>
    <div class="contact" style="top:452px">
      <span class="contact-icon"><svg width="20" height="20" viewBox="0 0 20 20"><rect x="2" y="4" width="16" height="12" rx="1.5" fill="#fff"/><path d="M2.5 5 10 11l7.5-6" fill="none" stroke="#f29a1f" stroke-width="1.6"/></svg></span>
      <span>info@brovana.info</span>
    </div>
  </div>
</section>

</body>
</html>
```